A new website for Electrical Contractor Business

We are looking for a unique and new WordPress website design which would include 5 Pages - Home Page, Meet the Team, Our Services, Our Projects and Contact Us page.

The global theme for the website needs to be professional but simple to navigate as we cater for both business and home owner customers.

Our core business service is targeted around lighting from single room decorative to large office so the theme should incorporate this in some way.

The home page should include;
Our business logo, Contact number, Email address, small Image rotation box - Highlighting pervious projectsText box - With welcome message, twitter feed news reel/Customer feed back box.

I would also like to see a 2 boxes for the separate customer types we services. Business and Home Owner. each box will have a small image with a small text description with a link to the area of the services page relevant to that customer type.

Meet the team page -This will be introducing potential customers to the team so I would like it to include for each team member. Something like a small image and text area which will introduce an outline of the team members skills and abilities.

Our Services page This page will be outlining the different services on offer to the both customer types business and homeowner. Each service should have an image with text description of the service would good here.

Our projects page-Will include images of pervious projects and work we have completed along with a text area for the project description/ outliner.

Contact Us page - Should include a contact form which should include an option for the customer to quest us to call them back, also a selection box for them to inform us our how they found our details would be good.

Colour - The theme colours can be taken from the logo or feel free to impress with your own imagination.

Remember we are looking for a website that will interest our customers enough to except our services or be drawn further into the website.. So call to action links to other areas of the site/ contact page are welcome

Target Market(s)

Business - Office, warehousing and Large Store - lighting and Power
Home owner lighting and power

Coding

Coded - Design and coding required

Number of Pages Required

5+ page

Font styles to use
Serif
Sans Serif

Colors

Designer to choose colors to be used in the design.

Requirements
Must have
• Logo integrated into the website design - i.e. website colours which allow the logo to blend into the design.
Nice to have
• Custom but professional theme catering to business customers, but also show that we do provide services to home owners too.
Should not have
• Sorry am not interested in one oversized block image on rotation covering half the home page.. Images will be needed but not a single block over sized frame with not text, shape. Please use your imagination when considering this design

```html
<!DOCTYPE html>
<html lang="en">
<head>
<meta charset="utf-8">
<title>Brightline Electric</title>
<link href="https://fonts.googleapis.com/css2?family=Audiowide&family=Open+Sans:wght@400;600;700&display=swap" rel="stylesheet">
<style>
:root{
  --orange:#f26a25;
  --navy:#1d2f5e;
  --ink:#111;
  --grey-bg:#f0f0f0;
  --text-grey:#666;
  --footer-bar:#1b1f27;
  --white:#fff;
}
*{margin:0;padding:0;box-sizing:border-box}
html,body{width:1200px;height:3551px;overflow:hidden}
body{font-family:"Open Sans",Arial,sans-serif;color:var(--ink);background:var(--white);position:relative}
.abs{position:absolute}
/* top bar */
.topbar{left:0;top:0;width:1200px;height:29px;background:#eee;font-size:9.5px;color:#333}
.topbar .call{left:698px;top:8px}
.topbar .mail{left:838px;top:8px}
.social-dots{left:1030px;top:7px;display:flex;gap:4px}
.social-dots span{width:15px;height:15px;border-radius:50%;background:#999;display:block}
.social-dots span:first-child{background:var(--navy)}
/* nav */
.nav{left:0;top:29px;width:1200px;height:64px;background:#fff;border-bottom:1px solid #ddd}
.brand{display:flex;align-items:center;gap:9px;font-weight:700;font-size:17px;color:var(--navy);letter-spacing:1px}
.brand .mark{width:30px;height:30px;border-radius:50%;background:var(--orange)}
.nav .brand{left:94px;top:17px}
.menu{left:563px;top:27px;display:flex;gap:25px;font-size:12px;color:#222}
.menu-cta{left:982px;top:21px;width:125px;height:29px;background:var(--navy);color:#fff;font-size:12px;font-weight:700;display:flex;align-items:center;justify-content:center;border-radius:2px}
/* hero */
.hero{left:0;top:93px;width:1200px;height:544px;overflow:hidden;
  background:
   radial-gradient(circle at 88% 8%,rgba(255,255,255,.85) 0,rgba(255,255,255,.25) 6%,transparent 14%),
   radial-gradient(ellipse 190px 210px at 79% 48%,#3f76b8 0,#24508c 40%,#15305a 70%,rgba(20,40,70,0) 100%),
   radial-gradient(ellipse 260px 150px at 58% 40%,rgba(60,170,220,.35),transparent 70%),
   linear-gradient(90deg,#030405 0%,#12171c 25%,#3d444b 50%,#79818a 75%,#9aa0a6 100%)}
.hero-line{font-family:"Audiowide",sans-serif;color:#fff;left:94px;line-height:1;white-space:nowrap}
.hero .l1{top:142px;font-size:39px}
.hero .l2{top:183px;font-size:66px;color:var(--orange)}
.hero .l3{top:261px;font-size:39px}
.hero .l4{top:302px;font-size:66px;color:var(--orange)}
.btn-white{background:#fff;color:var(--ink);font-weight:700;display:flex;align-items:center;justify-content:center}
.hero .btn-white{left:94px;top:410px;width:140px;height:40px;font-size:17px}
/* welcome */
.welcome{left:0;top:637px;width:1200px;height:382px;background:var(--grey-bg);overflow:hidden}
.welcome-photo{left:0;top:0;width:560px;height:382px;
  background:
   radial-gradient(ellipse 95px 110px at 55% 48%,#fffdf8 0,#f1e9da 60%,rgba(240,240,240,0) 100%),
   radial-gradient(ellipse 60px 50px at 26% 61%,#d9b25a 0,#a57f2c 60%,rgba(240,240,240,0) 100%),
   linear-gradient(180deg,#f3f3f3,#e9e9e9)}
.bolt{width:20px;height:32px}
.welcome .bolt{left:1078px;top:75px}
.eyebrow{color:var(--orange);font-size:17px}
.welcome .eyebrow{right:100px;top:109px}
.title{color:var(--navy);font-weight:700;font-size:38px;letter-spacing:.5px;white-space:nowrap}
.welcome .title{right:94px;top:128px}
.welcome p{right:94px;top:201px;width:560px;text-align:right;font-size:12.3px;line-height:17.2px;color:var(--text-grey)}
/* section heads */
.section-head{left:0;width:1200px;text-align:center}
.section-head .bolt{display:block;margin:0 auto}
.section-head .eyebrow{display:block;margin-top:2px;line-height:1.2}
.section-head .title{display:block;line-height:1.1}
.services-head{top:1088px}
/* service cards */
.card{width:448px;height:436px;background:#000;color:#fff;top:1229px}
.card .photo{width:100%;height:279px}
.card h3{font-weight:400;font-size:26px;text-align:center;margin-top:14px}
.card.home h3{margin-top:9px}
.card p{font-size:12.3px;line-height:17px;text-align:center;padding:6px 28px 0;font-weight:400}
.card.business{left:142px}
.card.business .photo{background:
   radial-gradient(ellipse 60px 120px at 53% 45%,#2f3fa8,#2a3a98 60%,transparent 100%),
   linear-gradient(90deg,#8a97b5 0%,#dfe4ec 20%,#c9d0db 40%,#2b3a96 52%,#d7dbe2 64%,#b9bcc2 85%,#8e9096 100%)}
.card.business .photo::after{content:"";display:block;height:100%;background:linear-gradient(180deg,rgba(255,255,255,.2) 0,transparent 30%,transparent 75%,rgba(255,255,255,.7) 88%,rgba(30,30,30,.6) 100%)}
.card.home{left:611px}
.card.home .photo{background:
   radial-gradient(ellipse 70px 90px at 48% 18%,rgba(230,235,255,.8),rgba(150,160,200,.2) 60%,transparent 100%),
   linear-gradient(90deg,#2a2f48 0%,#3a3a52 22%,#4b3427 38%,#6a4a34 70%,#4a3426 100%)}
.card.home .photo::after{content:"";display:block;height:100%;background:linear-gradient(180deg,rgba(20,25,60,.8) 0,transparent 35%,transparent 80%,rgba(220,215,210,.8) 92%,#2a2a2a 100%)}
/* projects */
.projects{left:0;top:1750px;width:1200px;height:799px;background:
  radial-gradient(ellipse 500px 300px at 28% 15%,rgba(90,55,80,.55),transparent 70%),
  radial-gradient(ellipse 400px 350px at 55% 90%,rgba(120,70,60,.5),transparent 70%),
  linear-gradient(110deg,#0b1230 0%,#1f2448 35%,#1a3566 60%,#0b1230 100%)}
.projects-head{top:70px}
.projects .title{color:#fff}
.tabs{top:203px;left:298px;display:flex;gap:8px}
.tab{width:196px;height:48px;background:#141414;color:#444;font-size:16px;display:flex;align-items:center;justify-content:center}
.tab.active{background:#fff;color:#111}
.tile{width:237px;height:184px}
.projects .btn-white{left:527px;top:724px;width:146px;height:33px;font-size:14px;color:var(--navy)}
/* testimonials */
.testi{left:94px;top:2635px;width:506px;height:382px;background:#171717;color:#fff}
.testi h2{position:absolute;left:30px;top:38px;font-size:24px;font-weight:700}
.quote{width:218px;font-size:11.5px;line-height:17px;color:#ccc}
.quote .avatar{width:50px;height:50px;border-radius:50%;background:radial-gradient(circle at 50% 40%,#e6e6e6,#9a9a9a 70%,#5e5e5e);margin-left:3px;margin-bottom:16px}
.quote .name{color:var(--orange);font-size:11.5px;margin-top:18px;font-weight:600;line-height:13px}
.quote .role{font-size:9px;color:#999;line-height:12px}
.testi .pager{left:36px;top:340px;width:20px;height:2px;background:#fff}
.partners{left:600px;top:2635px;width:506px;height:382px;background:var(--orange)}
.badge{background:#fff;width:44px;height:44px}
.badge.round{border-radius:50%}
/* footer */
.footer{left:0;top:3106px;width:1200px;height:378px;background:#000;color:#aaa;font-size:11.5px;line-height:16px}
.footer .brand{left:94px;top:75px;color:#fff}
.footer .brand .mark{background:#fff}
.footer h4{color:var(--orange);font-size:14px;font-weight:600}
.footer .about{left:94px;top:155px;width:245px}
.links{left:403px;top:150px;display:flex;flex-direction:column;gap:16px}
.contact-item{left:638px;width:200px}
.icon{left:600px;width:14px;height:14px}
.tweet{left:902px;display:flex;gap:8px;width:210px}
.tweet .thumb{width:40px;height:40px;flex:none}
.bottombar{left:0;top:3484px;width:1200px;height:67px;background:var(--footer-bar);color:#999;font-size:11px}
.bottombar .copy{left:94px;top:28px}
.bottom-social{left:956px;top:18px;display:flex;gap:10px}
.bottom-social span{width:30px;height:30px;border-radius:50%;background:#777;display:block}
</style>
</head>
<body>

<div class="abs topbar">
  <span class="abs call">Call:&nbsp;&nbsp;&nbsp;(00) 987 6543 210</span>
  <span class="abs mail">Email:&nbsp;&nbsp;&nbsp;info@brightline-electric.com</span>
  <div class="abs social-dots"><span></span><span></span><span></span><span></span></div>
</div>

<header class="abs nav">
  <div class="abs brand"><span class="mark"></span>BRIGHTLINE</div>
  <nav class="abs menu"><span>Home</span><span>Meet the Team</span><span>Our Services</span><span>Projects</span><span>Contact Us</span></nav>
  <div class="abs menu-cta">Pervious Projects</div>
</header>

<section class="abs hero" role="img" aria-label="Light bulb lying on its side with the Earth glowing inside, on a grey surface">
  <div class="abs hero-line l1">AROUND LIGHTING FROM</div>
  <div class="abs hero-line l2">SINGLE ROOM</div>
  <div class="abs hero-line l3">DECORATIVE TO</div>
  <div class="abs hero-line l4">LARGE OFFICE</div>
  <div class="abs btn-white">View More</div>
</section>

<section class="abs welcome">
  <div class="abs welcome-photo" role="img" aria-label="Clear filament light bulb with brass base"></div>
  <svg class="abs bolt" viewBox="0 0 20 32"><path d="M12 0 L2 18 H9 L6 32 L18 12 H11 L14 0Z" fill="#f26a25"/></svg>
  <div class="abs eyebrow">Welcome To</div>
  <div class="abs title">BRIGHTLINE ELECTRIC</div>
  <p class="abs">Sed vitae tortor ac orci pharetra dictum ac at augue. Duis sed mauris sem. Fusce vel velit varius, mattis ligula eu, interdum augue. Aenean eget semper nunc, non fringilla tellus. Fusce lorem augue, sagittis sit amet libero a, porttitor dictum risus. Morbi consequat lacus mauris, sit amet ultrices risus porttitor a. Curabitur laoreet quam eu hendrerit lobortis. Nam vel elementum augue. Phasellus quis sem sed erat maximus tincidunt vitae id justo. Donec quis est turpis. Vivamus suscipit sapien in risus lobortis, vel viverra ipsum hendrerit.</p>
</section>

<div class="abs section-head services-head">
  <svg class="bolt" viewBox="0 0 20 32"><path d="M12 0 L2 18 H9 L6 32 L18 12 H11 L14 0Z" fill="#f26a25"/></svg>
  <span class="eyebrow">Brightline Electric</span>
  <span class="title">SERVICES</span>
</div>

<article class="abs card business">
  <div class="photo" role="img" aria-label="Modern office lobby with glass meeting room and blue feature wall"></div>
  <h3>Business Services</h3>
  <p>Lorem ipsum dolor sit amet, consectetur adipiscing elit. Sed vel iaculis dui, et vehicula lectus. Aenean ullamcorper scelerisque tortor, vitae scelerisque ex dapibus vitae. Proin risus risus, hendrerit lobortis lacus consectetur, ultricies vestibulum sapien.</p>
</article>
<article class="abs card home">
  <div class="photo" role="img" aria-label="Living room with crystal chandelier and wood panel wall"></div>
  <h3>Home Owner Services</h3>
  <p>Lorem ipsum dolor sit amet, consectetur adipiscing elit. Sed vel iaculis dui, et vehicula lectus. Aenean ullamcorper scelerisque tortor, vitae scelerisque ex dapibus vitae. Proin risus risus, hendrerit lobortis lacus consectetur, ultricies vestibulum sapien.</p>
</article>

<section class="abs projects">
  <div class="abs section-head projects-head">
    <svg class="bolt" viewBox="0 0 20 32"><path d="M12 0 L2 18 H9 L6 32 L18 12 H11 L14 0Z" fill="#f26a25"/></svg>
    <span class="eyebrow">Brightline Electric</span>
    <span class="title">PROJECTS</span>
  </div>
  <div class="abs tabs"><div class="tab active">All</div><div class="tab">Business</div><div class="tab">Home Owner</div></div>
  <div class="abs tile" style="left:94px;top:284px;background:linear-gradient(180deg,#e4e0da 0%,#c9c2b8 35%,#6b4e5e 55%,#8a6e54 80%,#f1efeb 100%)" role="img" aria-label="Dining room with pendant lights"></div>
  <div class="abs tile" style="left:352px;top:284px;background:radial-gradient(ellipse at 55% 65%,#fbe9d0,#e9bf8c 45%,#8c7046 85%,#4a4a38 100%)" role="img" aria-label="Hanging plants with pendant lamps"></div>
  <div class="abs tile" style="left:611px;top:284px;background:radial-gradient(ellipse at 45% 45%,#f1e2bd,#c09a52 40%,#6e4e22 75%,#2e2010 100%)" role="img" aria-label="Crystal chandelier"></div>
  <div class="abs tile" style="left:869px;top:284px;background:radial-gradient(ellipse at 50% 55%,#8a8d86,#40464c 45%,#1c2228 100%)" role="img" aria-label="Globe lights among hanging vines"></div>
  <div class="abs tile" style="left:94px;top:494px;background:linear-gradient(180deg,#7a5526 0%,#3a2a1a 25%,#2a2420 70%,#4a3a22 100%)" role="img" aria-label="Bare bulbs hanging in a dark room"></div>
  <div class="abs tile" style="left:352px;top:494px;background:radial-gradient(ellipse at 50% 50%,#fff1dc,#f2c79a 45%,#c98656 80%,#6a3a22 100%)" role="img" aria-label="Paper lantern pendant lights"></div>
  <div class="abs tile" style="left:611px;top:494px;background:radial-gradient(ellipse at 55% 60%,#f0a040,#a2482c 35%,#4a1a32 70%,#150812 100%)" role="img" aria-label="Glass drop pendant bulbs"></div>
  <div class="abs tile" style="left:869px;top:494px;background:linear-gradient(180deg,#2a2a2a 0%,#5c5a52 40%,#b8b6aa 75%,#e2e0d8 100%)" role="img" aria-label="Restaurant hall with hanging bulbs"></div>
  <div class="abs btn-white">View More</div>
</section>

<section class="abs testi">
  <h2>TESTIMONIALS</h2>
  <div class="abs quote" style="left:30px;top:118px">
    <div class="avatar" role="img" aria-label="Customer portrait"></div>
    Morbi mollis blandit aliquet. Fusce cursus, eros in euismod tristique, elit ipsum eleifend nulla, vitae euismod odio purus eget nunc.
    <div class="name">Clara Benton</div><div class="role">CEO, Business Group</div>
  </div>
  <div class="abs quote" style="left:258px;top:118px">
    <div class="avatar" role="img" aria-label="Customer portrait"></div>
    Morbi mollis blandit aliquet. Fusce cursus, eros in euismod tristique, elit ipsum eleifend nulla, vitae euismod odio purus eget nunc.
    <div class="name">Clara Benton</div><div class="role">CEO, Business Group</div>
  </div>
  <div class="abs pager"></div>
</section>

<section class="abs partners" aria-label="Partner badges">
  <div class="abs badge round" style="left:45px;top:50px"></div>
  <div class="abs badge" style="left:170px;top:50px"></div>
  <div class="abs badge round" style="left:281px;top:50px"></div>
  <div class="abs badge" style="left:396px;top:50px"></div>
  <div class="abs badge" style="left:45px;top:150px"></div>
  <div class="abs badge round" style="left:170px;top:150px"></div>
  <div class="abs badge" style="left:281px;top:150px"></div>
  <div class="abs badge round" style="left:396px;top:150px"></div>
  <div class="abs badge round" style="left:45px;top:262px"></div>
  <div class="abs badge" style="left:165px;top:262px"></div>
  <div class="abs badge round" style="left:281px;top:262px"></div>
  <div class="abs badge" style="left:396px;top:262px"></div>
</section>

<footer class="abs footer">
  <div class="abs brand"><span class="mark"></span>BRIGHTLINE</div>
  <p class="abs about">Morbi mollis blandit aliquet. Fusce cursus, eros in euismod tristique, elit ipsum eleifend nulla, vitae euismod odio purus eget nunc. Donec dignissim auctor massa, non faucibus nisl porta pellentesque. Nam laoreet vel metus at porta. Nulla condimentum luctus quam, sit amet gravida odio.</p>
  <h4 class="abs" style="left:403px;top:82px">IMPORTANT LINKS</h4>
  <div class="abs links"><span>Home</span><span>Meet the Team</span><span>Our Services</span><span>Projects</span><span>Contact Us</span></div>
  <h4 class="abs" style="left:600px;top:82px">QUICK CONTACT</h4>
  <svg class="abs icon" style="top:155px" viewBox="0 0 14 14"><path d="M7 1a4 4 0 0 0-4 4c0 3 4 8 4 8s4-5 4-8a4 4 0 0 0-4-4z" fill="#f26a25"/><circle cx="7" cy="5" r="1.5" fill="#000"/></svg>
  <p class="abs contact-item" style="top:150px">Morbi mollis blandit aliquet. Fusce cursus, eros in euismod tristique, elit ipsum eleifend nulla.</p>
  <svg class="abs icon" style="top:222px" viewBox="0 0 14 14"><path d="M3 1l2 3-1.5 1.5c1 2 2.5 3.5 4.5 4.5L9.5 8.5l3 2-1.5 2.5C6 13 1 8 1 2.5z" fill="#f26a25"/></svg>
  <p class="abs contact-item" style="top:218px">(+00) 987 6543 210<br>(+00) 987 6543 210</p>
  <svg class="abs icon" style="top:268px" viewBox="0 0 14 14"><rect x="1" y="3" width="12" height="8" fill="#f26a25"/><path d="M1 3l6 5 6-5" stroke="#000" fill="none"/></svg>
  <p class="abs contact-item" style="top:266px">info@brightline-electric.com</p>
  <h4 class="abs" style="left:902px;top:82px">TWITTER MESSAGE</h4>
  <div class="abs tweet" style="top:154px"><span class="thumb" role="img" aria-label="Tweet image" style="background:radial-gradient(circle,#d8c8b8,#5a4a44 70%)"></span><span>Morbi mollis blandit aliquet. Fusce cursus, eros in euismod tristique.</span></div>
  <div class="abs tweet" style="top:219px"><span class="thumb" role="img" aria-label="Tweet image" style="background:linear-gradient(135deg,#2a2230,#b88a4a 55%,#3a2a1e)"></span><span>Morbi mollis blandit aliquet. Fusce cursus, eros in euismod tristique.</span></div>
  <div class="abs tweet" style="top:284px"><span class="thumb" role="img" aria-label="Tweet image" style="background:radial-gradient(circle,#c8883a,#4a2a1a 70%)"></span><span>Morbi mollis blandit aliquet. Fusce cursus, eros in euismod tristique.</span></div>
</footer>

<div class="abs bottombar">
  <span class="abs copy">Copyright © 2019 Brightline Electric. All Rights Reserved.</span>
  <div class="abs bottom-social"><span></span><span></span><span></span><span></span></div>
</div>

</body>
</html>
```